Profile and Wizard Based Website

The scope of this project is to create a website that will allow users to signup through a wizard. The wizard is already made and will be provided.

Users should also be able to login using their pallnook account and then the wizard will start.

After the the wizard is complete and all the information is captured, the user will have a dashboard that will display different information in different sections of dashboard.

The website will also have different levels of access; user, moderator and admin.

The admin will have the ability to see data reports based on the user information captured from the website.

Deliverables:

- Layouts for login page
- Layouts for the wizard questions (about 10 questions in the wizard, each page will display one question)
- Layouts for Dashboard/Profile login
- Layouts for content and document library (Documents, Videos etc)

More info to come.

Attached is the sample wizard question layout and flow chart for wizard.

```html
<!DOCTYPE html>
<html lang="en">
<head>
<meta charset="utf-8">
<title>Brightpath – Wizard Question</title>
<link href="https://fonts.googleapis.com/css2?family=Source+Sans+3:wght@400;600;700&family=Quicksand:wght@400&family=Open+Sans:wght@300;400&display=swap" rel="stylesheet">
<style>
  :root{
    --page:#f7f8f8;
    --hero-top:#f3f4f4;
    --hero-bottom:#eceded;
    --line:#e4e6e6;
    --blue:#3f7bc4;
    --blue-light:#5b90d2;
    --blue-dark:#2f67ad;
    --grey-text:#9a9a9a;
    --dark-text:#4a4a4a;
    --digit:#cbcbcb;
    --track:#e2e2e2;
    --button:#e5e5e5;
  }
  *{box-sizing:border-box;margin:0;padding:0}
  html,body{width:1105px;height:1200px;overflow:hidden;background:var(--page)}
  body{font-family:"Source Sans 3",Arial,sans-serif;position:relative;border:1px solid #d6d8d8}
  .site-header{position:absolute;left:0;top:0;width:100%;height:74px;border-bottom:1px solid var(--line);background:var(--page);z-index:3}
  .brand{position:absolute;left:65px;top:26px;display:flex;align-items:center;gap:12px}
  .brand-mark{width:22px;height:22px;border-radius:50%;background:var(--blue)}
  .brand-name{font-weight:700;font-size:17px;color:var(--blue);letter-spacing:.2px}
  .main-nav{position:absolute;left:0;right:0;top:28px;text-align:center;font-size:15px;font-weight:600;color:var(--grey-text);padding-left:52px}
  .main-nav a{color:var(--grey-text);text-decoration:none}
  .main-nav a.is-active{color:var(--blue)}
  .main-nav .sep{margin:0 9px;color:#c5c5c5;font-weight:400}
  .user{position:absolute;right:90px;top:12px;display:flex;align-items:center;gap:24px}
  .user-name{font-family:"Open Sans",Arial,sans-serif;font-size:15px;color:var(--dark-text)}
  .avatar{width:52px;height:52px;border-radius:50%;border:3px solid #5a5a5a;background:radial-gradient(circle at 50% 45%,#d9a63a,#6b4a1c 60%,#1e1a16)}
  .hero{position:absolute;left:0;top:74px;width:100%;height:504px;background:linear-gradient(180deg,var(--hero-top) 0%,var(--hero-top) 45%,var(--hero-bottom) 100%);overflow:hidden}
  .hero svg{position:absolute;left:0;top:0}
  .question{position:absolute;left:0;right:0;top:638px;text-align:center;font-family:"Open Sans",Arial,sans-serif;font-weight:400;font-size:25px;color:var(--dark-text);padding-left:22px}
  .divider{position:absolute;left:242px;width:645px;height:1px;background:var(--line)}
  .slider{position:absolute;left:126px;top:780px}
  .rating-label{position:absolute;left:0;right:0;top:868px;text-align:center;font-weight:700;font-size:36px;color:var(--blue);padding-left:22px}
  .next-button{position:absolute;left:520px;top:1015px;width:88px;height:88px;border-radius:50%;background:var(--button);border:none;font-family:"Source Sans 3",Arial,sans-serif;font-weight:700;font-size:18px;color:#a5a5a5}
  .site-footer{position:absolute;left:0;top:1129px;width:100%;border-top:1px solid var(--line);height:71px;font-size:15px;font-weight:600;color:var(--grey-text)}
  .footer-links{position:absolute;left:43px;top:28px}
  .footer-links a{color:var(--grey-text);text-decoration:none}
  .footer-links a.is-active{color:var(--blue)}
  .footer-links .sep{margin:0 9px;color:#c5c5c5;font-weight:400}
  .copyright{position:absolute;right:90px;top:28px}
</style>
</head>
<body>
  <header class="site-header">
    <div class="brand"><span class="brand-mark"></span><span class="brand-name">BRIGHTPATH</span></div>
    <nav class="main-nav">
      <a href="#">MENU 1</a><span class="sep">/</span><a href="#" class="is-active">MENU 2</a><span class="sep">/</span><a href="#">MENU 3</a><span class="sep">/</span><a href="#">MENU 4</a>
    </nav>
    <div class="user"><span class="user-name">Dana Whitfield</span><div class="avatar" role="img" aria-label="User profile photo"></div></div>
  </header>

  <section class="hero">
    <svg width="1105" height="504" viewBox="0 74 1105 504" role="img" aria-label="Fluency score 83 percent over a soft backdrop">
      <circle class="score-frame" cx="586" cy="472" r="317" fill="#f8f9f9"/>
      <circle cx="586" cy="472" r="262" fill="none" stroke="#dfe1e1" stroke-width="1.5"/>
      <circle class="score-disc" cx="586" cy="472" r="222" fill="#f1f2f2" stroke="#e3e4e4"/>
      <circle class="score-arc-track" cx="586" cy="472" r="246" fill="none" stroke="#ffffff" stroke-width="22"/>
      <g transform="rotate(31 586 472)">
        <circle class="score-arc" cx="586" cy="472" r="246" fill="none" stroke="var(--blue-light)" stroke-width="20" stroke-dasharray="1283 1546"/>
        <circle cx="586" cy="472" r="240" fill="none" stroke="var(--blue)" stroke-width="8" stroke-dasharray="1252 1508"/>
      </g>
      <text class="score-value" x="580" y="566" text-anchor="middle" font-family="Quicksand, sans-serif" font-size="300" fill="var(--digit)" letter-spacing="-10">83</text>
      <text class="score-unit" x="744" y="348" font-family="Open Sans, sans-serif" font-size="24" fill="#a0a0a0">%</text>
    </svg>
  </section>

  <h1 class="question">Rate your English fluency</h1>
  <div class="divider" style="top:696px"></div>

  <svg class="slider" width="860" height="60" viewBox="0 0 860 60" role="slider" aria-valuenow="45" aria-label="Fluency rating">
    <path d="M0 6 L845 6 L852 14 L852 54 L0 54 Z" fill="var(--track)"/>
    <path d="M0 6 L845 6 L852 14 L0 14 Z" fill="#ececec"/>
    <rect x="0" y="14" width="452" height="40" fill="var(--blue)"/>
    <path d="M0 6 L452 6 L452 14 L0 14 Z" fill="var(--blue-light)"/>
    <rect x="0" y="50" width="852" height="4" fill="#d2d2d2"/>
    <rect x="0" y="50" width="452" height="4" fill="var(--blue-dark)"/>
    <line x1="20" y1="30" x2="430" y2="30" stroke="#2d5f9f" stroke-width="1.5"/>
    <line x1="470" y1="30" x2="830" y2="30" stroke="#c4c4c4" stroke-width="1.5"/>
    <g fill="#2d5f9f">
      <circle cx="24" cy="30" r="2.5"/><circle cx="47" cy="30" r="2.5"/><circle cx="70" cy="30" r="2.5"/><circle cx="93" cy="30" r="2.5"/><circle cx="116" cy="30" r="2.5"/><circle cx="139" cy="30" r="2.5"/><circle cx="162" cy="30" r="2.5"/><circle cx="185" cy="30" r="2.5"/><circle cx="208" cy="30" r="2.5"/><circle cx="231" cy="30" r="2.5"/><circle cx="254" cy="30" r="2.5"/><circle cx="277" cy="30" r="2.5"/><circle cx="300" cy="30" r="2.5"/><circle cx="323" cy="30" r="2.5"/><circle cx="346" cy="30" r="2.5"/><circle cx="369" cy="30" r="2.5"/><circle cx="392" cy="30" r="2.5"/><circle cx="415" cy="30" r="2.5"/>
    </g>
    <g fill="#bdbdbd">
      <circle cx="485" cy="30" r="2.5"/><circle cx="508" cy="30" r="2.5"/><circle cx="531" cy="30" r="2.5"/><circle cx="554" cy="30" r="2.5"/><circle cx="577" cy="30" r="2.5"/><circle cx="600" cy="30" r="2.5"/><circle cx="623" cy="30" r="2.5"/><circle cx="646" cy="30" r="2.5"/><circle cx="669" cy="30" r="2.5"/><circle cx="692" cy="30" r="2.5"/><circle cx="715" cy="30" r="2.5"/><circle cx="738" cy="30" r="2.5"/><circle cx="761" cy="30" r="2.5"/><circle cx="784" cy="30" r="2.5"/><circle cx="807" cy="30" r="2.5"/><circle cx="830" cy="30" r="2.5"/>
    </g>
    <g class="slider-thumb">
      <rect x="434" y="23" width="40" height="22" rx="5" fill="#d7d7d7" stroke="#8f8f8f"/>
      <path d="M449 29 L445 34 L449 39 M459 29 L463 34 L459 39" fill="none" stroke="#555" stroke-width="1.6"/>
    </g>
  </svg>

  <p class="rating-label">NEED IMPROVEMENT</p>
  <div class="divider" style="top:992px"></div>

  <button class="next-button" type="button">NEXT</button>

  <footer class="site-footer">
    <nav class="footer-links"><a href="#">HOW IT WORKS</a><span class="sep">/</span><a href="#" class="is-active">TERMS &amp; CONDITIONS</a><span class="sep">/</span><a href="#">CONTACT</a></nav>
    <p class="copyright">COPYRIGHT © 2014 NORTHWIND. ALL RIGHTS RESERVED.</p>
  </footer>
</body>
</html>
```